Kestrel Plumbing business card full re design & logo design

Kestrel Plumbing is a Sydney based mechanical plumbing contractor company.
We would like a full redesign with new logo etc which we can take to a future website, uniforms, vehicle sign writing etc.
Blue is my preferred choice of colour but i would be open to see a couple of alternatives thrown in the mix to see how they compare. I am open to see on white cards, black cards etc. Open to many new ideas.
Please see attached original business cards which have been used for the last 5 years.

Target Market(s)

Mechanical services industry.

Industry/Entity Type

Plumbing

Contact Information for Business Card

Dale Fenmore
Director

Mob: 0427 596 418
Email: dale@kestrelplumbing-demo.net.au
PO BOX 782
Merrowfield NSW 2157
Lic: 518604k

Logo Text

Kestrel Plumbing

Font styles to use
Sans Serif

Colors
0655a3
3276b5
0792cd
33a6d7
85cae6
000000
333333
474747

Requirements
Must have
• Things that make it very professional and very well presented.
Nice to have
• Same description or very similar to attached uploaded file
Should not have
• Anything that makes it look unprofessional or cartoony.

```html
<!DOCTYPE html>
<html lang="en">
<head>
<meta charset="utf-8">
<title>Kestrel Plumbing – Business Card Set</title>
<link href="https://fonts.googleapis.com/css2?family=Roboto+Condensed:wght@400;700&display=swap" rel="stylesheet">
<style>
  :root {
    --navy: #034672;
    --brand-blue: #2f74a8;
    --steel: #8fb0d2;
    --ink: #1f1f1f;
    --paper: #ffffff;
    --page: #ffffff;
    --edge: #d9dde2;
  }
  * { margin: 0; padding: 0; box-sizing: border-box; }
  html, body {
    width: 1165px; height: 1200px; overflow: hidden;
    background: var(--page);
    font-family: "Roboto Condensed", "Arial Narrow", sans-serif;
  }
  .canvas { position: relative; width: 1165px; height: 1200px; }

  /* Contact side of the card */
  .card-back {
    position: absolute; left: 182px; top: 190px;
    width: 600px; height: 350px;
    background: var(--paper);
    border: 1px solid var(--edge);
    box-shadow: 0 6px 18px rgba(0,0,0,.12);
    color: var(--ink);
  }
  .card-back .name {
    position: absolute; left: 40px; top: 58px;
    font-weight: 700; font-size: 27px; color: var(--brand-blue);
  }
  .card-back .role {
    position: absolute; left: 40px; top: 94px; font-size: 20px;
  }
  .card-back .wordmark {
    position: absolute; right: 40px; top: 62px;
    font-weight: 700; font-size: 34px; color: var(--steel);
    letter-spacing: .5px;
  }
  .card-back .licence {
    position: absolute; left: 40px; top: 178px;
    font-weight: 700; font-size: 21px; color: var(--brand-blue);
  }
  .card-back .trade {
    position: absolute; left: 40px; top: 204px; font-size: 21px;
  }
  .card-back .phone {
    position: absolute; left: 40px; top: 284px; font-size: 21px; letter-spacing: .5px;
  }
  .card-back .divider {
    position: absolute; left: 198px; top: 258px;
    width: 3px; height: 58px; background: var(--brand-blue);
  }
  .card-back .address {
    position: absolute; left: 212px; top: 258px; font-size: 19px; line-height: 28px;
    white-space: nowrap;
  }

  /* Brand side of the card */
  .card-front {
    position: absolute; left: 27px; top: 838px;
    width: 587px; height: 358px;
    background: var(--navy);
  }
  .card-front .wordmark {
    position: absolute; left: 0; right: 0; top: 118px;
    text-align: center;
    font-weight: 700; font-size: 56px; color: var(--steel);
  }
  .card-front .tagline {
    position: absolute; left: 0; right: 0; top: 232px;
    text-align: center;
    font-weight: 700; font-size: 24px; color: var(--paper);
  }

  /* Logo lock-up on white */
  .logo-white {
    position: absolute; left: 770px; top: 938px; width: 395px;
    text-align: center;
  }
  .logo-white .wordmark {
    font-weight: 700; font-size: 52px; color: var(--steel);
  }
  .logo-white .tagline {
    margin-top: 40px;
    font-weight: 700; font-size: 23px; color: var(--navy);
    white-space: nowrap;
  }
</style>
</head>
<body>
<main class="canvas">

  <section class="card-back" aria-label="Business card, contact side">
    <div class="name">Dale Fenmore</div>
    <div class="role">Director</div>
    <div class="wordmark">Kestrel Plumbing</div>
    <div class="licence">LIC: 518604k</div>
    <div class="trade">MECHANICAL PLUMBING CONTRACTOR</div>
    <div class="phone">0427 596 418</div>
    <div class="divider"></div>
    <div class="address">
      PO BOX 782 Merrowfield NSW 2157<br>
      Email: dale@kestrelplumbing-demo.net.au
    </div>
  </section>

  <section class="card-front" aria-label="Business card, brand side">
    <div class="wordmark">Kestrel Plumbing</div>
    <div class="tagline">MECHANICAL PLUMBING CONTRACTOR</div>
  </section>

  <section class="logo-white" aria-label="Logo on white">
    <div class="wordmark">Kestrel Plumbing</div>
    <div class="tagline">MECHANICAL PLUMBING CONTRACTOR</div>
  </section>

</main>
</body>
</html>
```